CRANDEL'S needs a label design for a Moruga Scorpion Pepper Hot Sauce (5oz bottle)

We need a label for a new company based in south Mississippi called CRANDEL'S. We have a new hot sauce made from Moruga Scorpion Peppers that's very hot yet has "layers of flavor". The sauce is a deep red color in a clear bottle. We are looking for something simple yet different and will stand out. We would like to limit the design to 3 colors.

• wide latin?

```html
<!DOCTYPE html>
<html lang="en">
<head>
<meta charset="utf-8">
<title>CRANDEL'S Moruga Scorpion Pepper Hot Sauce Label</title>
<link rel="stylesheet" href="https://fonts.googleapis.com/css2?family=Tinos:wght@400;700&family=Ultra&display=swap">
<style>
  :root {
    --paper: #ffffff;
    --cap: #141414;
    --glass: #f3f0ea;
    --sauce: #3b1313;
    --label: #0e0d0d;
    --pepper-red: #b01818;
    --ink-light: #f4f1ec;
  }
  html, body {
    margin: 0;
    padding: 0;
    width: 1200px;
    height: 3927px;
    overflow: hidden;
    background: var(--paper);
  }
  .bottle {
    position: relative;
    width: 1200px;
    height: 3927px;
  }
  .bottle-shape {
    position: absolute;
    inset: 0;
  }
  .label {
    position: absolute;
    left: 0;
    top: 2016px;
    width: 1200px;
    height: 1500px;
    text-align: center;
  }
  .label > * {
    position: absolute;
    left: 0;
    width: 100%;
    margin: 0;
    white-space: nowrap;
  }
  .brand-name {
    top: 262px;
    font-family: "Tinos", serif;
    font-weight: 700;
    font-size: 128px;
    line-height: 1;
    letter-spacing: 2px;
    color: var(--ink-light);
  }
  .product-name {
    top: 660px;
    font-family: "Ultra", serif;
    font-size: 150px;
    line-height: 1;
    letter-spacing: 8px;
    color: var(--pepper-red);
  }
  .product-variety {
    top: 814px;
    font-family: "Ultra", serif;
    font-size: 54px;
    line-height: 1;
    letter-spacing: 3px;
    color: var(--pepper-red);
  }
  .heat-level {
    top: 992px;
    font-family: "Tinos", serif;
    font-weight: 400;
    font-size: 72px;
    line-height: 1;
    color: var(--ink-light);
  }
  .pepper-art {
    top: 1270px;
    left: 426px;
    width: 444px !important;
    height: 180px;
    border-radius: 46% 46% 40% 40%;
    background: radial-gradient(ellipse at 50% 45%, #d8251f 0%, #a5130f 60%, #4a0808 100%);
  }
</style>
</head>
<body>
<main class="bottle">
  <svg class="bottle-shape" width="1200" height="3927" viewBox="0 0 1200 3927" aria-hidden="true">
    <path class="bottle-cap" d="M206 40 Q206 4 246 4 L960 4 Q1000 4 1000 40 L1000 150 L206 150 Z" fill="var(--cap)"/>
    <path class="bottle-neck" d="M228 150 L978 150 L866 526 L334 526 Z" fill="var(--glass)"/>
    <path class="bottle-body" d="M334 526 L866 526 L1200 1990 L1200 3890 Q1200 3922 1168 3922 L32 3922 Q0 3922 0 3890 L0 1990 Z" fill="var(--sauce)"/>
    <rect class="bottle-label-band" x="0" y="2016" width="1200" height="1500" fill="var(--label)"/>
  </svg>

  <section class="label">
    <h1 class="brand-name">CRANDEL'S</h1>
    <h2 class="product-name">MORUGA</h2>
    <p class="product-variety">SCORPION PAPPER</p>
    <p class="heat-level">VERY HOT</p>
    <div class="pepper-art" role="img" aria-label="Illustration of two red Moruga Scorpion peppers"></div>
  </section>
</main>
</body>
</html>
```